Brimovex business card

Based on company logo and website given , to design a business card temple. Slogan "Your furry friends deserves the best"
Color style please refer to our website

```html
<!DOCTYPE html>
<html lang="en">
<head>
<meta charset="utf-8">
<title>Brimovex business card</title>
<link rel="stylesheet" href="https://fonts.googleapis.com/css2?family=Arimo:wght@400&family=Libre+Baskerville:wght@400;700&family=Oswald:wght@500&display=swap">
<style>
  :root {
    --stage: #202020;
    --card: #0b0b0b;
    --gold: #c3b43a;
    --silver: #d9d9d9;
    --text: #cfcfcf;
    --muted: #a9a9a9;
    --rule: #5a5a5a;
    --badge-green: #1d8a3f;
    --badge-gold: #d6ad3c;
    --badge-red: #c8202b;
    --social-blue: #3b5998;
    --social-pink: #d6336c;
  }
  * { box-sizing: border-box; margin: 0; padding: 0; }
  html, body { width: 1200px; height: 900px; overflow: hidden; }
  body {
    background: var(--stage);
    display: flex;
    align-items: center;
    justify-content: center;
    gap: 40px;
  }
  .card {
    position: relative;
    width: 540px;
    height: 330px;
    background: var(--card);
    border-radius: 18px;
    overflow: hidden;
  }

  /* Front: contact side */
  .front .brand {
    position: absolute;
    left: 34px;
    top: 196px;
    width: 226px;
    display: flex;
    align-items: center;
    gap: 8px;
    white-space: nowrap;
    font-family: "Libre Baskerville", serif;
    font-weight: 700;
    font-size: 34px;
    line-height: 1;
    color: var(--gold);
  }
  .front .brand-dot {
    width: 10px; height: 10px; border-radius: 50%;
    flex: none;
    background: var(--gold);
  }
  .front .divider {
    position: absolute;
    left: 276px; top: 60px;
    width: 1px; height: 210px;
    background: var(--rule);
  }
  .front .details {
    position: absolute;
    left: 298px; top: 62px;
    width: 226px;
  }
  .person-name {
    font-family: "Libre Baskerville", serif;
    font-size: 18px;
    letter-spacing: 0.5px;
    color: var(--gold);
    text-transform: uppercase;
    white-space: nowrap;
  }
  .person-role {
    font-family: "Arimo", sans-serif;
    font-size: 14px;
    color: var(--muted);
    margin-top: 2px;
  }
  .contact-list { list-style: none; margin-top: 16px; }
  .contact-list li {
    display: flex; align-items: center; gap: 8px;
    font-family: "Arimo", sans-serif;
    font-size: 14px;
    color: var(--text);
    line-height: 22px;
    white-space: nowrap;
  }
  .contact-icon { width: 16px; height: 16px; flex: none; }
  .address {
    margin-top: 18px;
    font-family: "Arimo", sans-serif;
    font-size: 14px;
    line-height: 19px;
    color: var(--text);
  }

  /* Back: brand side */
  .back .brand {
    position: absolute;
    left: 0; right: 0; top: 62px;
    text-align: center;
    font-family: "Libre Baskerville", serif;
    font-weight: 700;
    font-size: 50px;
    color: var(--silver);
  }
  .back .rule {
    position: absolute;
    height: 1px;
    background: var(--rule);
  }
  .back .rule.top-left { left: 90px; width: 150px; top: 158px; }
  .back .rule.top-right { right: 90px; width: 150px; top: 158px; }
  .back .rule.bottom { left: 90px; right: 90px; top: 202px; }
  .social {
    position: absolute;
    left: 50%; top: 146px;
    transform: translateX(-50%);
    display: flex; gap: 8px;
  }
  .social span { width: 24px; height: 24px; border-radius: 50%; }
  .social .blue { background: var(--social-blue); }
  .social .pink { background: var(--social-pink); }
  .slogan {
    position: absolute;
    left: 0; right: 0; top: 170px;
    text-align: center;
    font-family: "Oswald", sans-serif;
    font-weight: 500;
    font-size: 19px;
    letter-spacing: 0.3px;
    color: var(--silver);
    text-transform: uppercase;
  }
  .badges {
    position: absolute;
    left: 50%; top: 222px;
    transform: translateX(-50%);
    display: flex; gap: 18px;
  }
  .badge { width: 62px; height: 62px; border-radius: 50%; }
  .badge.green { background: var(--badge-green); border: 4px solid #fff; }
  .badge.gold { background: var(--badge-gold); border: 4px solid var(--badge-red); }
</style>
</head>
<body>

  <section class="card front" aria-label="Business card front">
    <div class="brand"><span class="brand-dot"></span>Brimovex</div>
    <div class="divider"></div>
    <div class="details">
      <p class="person-name">Marcus Hale</p>
      <p class="person-role">Managing Director</p>
      <ul class="contact-list">
        <li>
          <svg class="contact-icon" viewBox="0 0 16 16"><rect width="16" height="16" rx="2" fill="#c3b43a"/><path d="M4.5 3.5l2 0 .8 2.3-1.2.9a6 6 0 0 0 3.2 3.2l.9-1.2 2.3.8v2a1 1 0 0 1-1 1A8.5 8.5 0 0 1 3.5 4.5a1 1 0 0 1 1-1z" fill="#0b0b0b"/></svg>
          +61 3 9041 2286
        </li>
        <li>
          <svg class="contact-icon" viewBox="0 0 16 16"><rect width="16" height="16" rx="2" fill="#c3b43a"/><rect x="5" y="2.5" width="6" height="11" rx="1" fill="none" stroke="#0b0b0b" stroke-width="1.4"/><circle cx="8" cy="11.5" r=".7" fill="#0b0b0b"/></svg>
          1800 417 390
        </li>
        <li>
          <svg class="contact-icon" viewBox="0 0 16 16"><rect width="16" height="16" rx="2" fill="#c3b43a"/><circle cx="8" cy="8" r="5" fill="none" stroke="#0b0b0b" stroke-width="1.2"/><path d="M3 8h10M8 3c-2 2.5-2 7.5 0 10M8 3c2 2.5 2 7.5 0 10" fill="none" stroke="#0b0b0b" stroke-width="1"/></svg>
          www.brimovex.com.au
        </li>
        <li>
          <svg class="contact-icon" viewBox="0 0 16 16"><rect width="16" height="16" rx="2" fill="#c3b43a"/><rect x="3" y="4.5" width="10" height="7" fill="none" stroke="#0b0b0b" stroke-width="1.2"/><path d="M3 4.5l5 4 5-4" fill="none" stroke="#0b0b0b" stroke-width="1.2"/></svg>
          sales@brimovex.com.au
        </li>
      </ul>
      <p class="address">4/22 Carrow Street<br>Ashvale Vic 3190</p>
    </div>
  </section>

  <section class="card back" aria-label="Business card back">
    <div class="brand">Brimovex</div>
    <div class="rule top-left"></div>
    <div class="rule top-right"></div>
    <div class="social"><span class="blue"></span><span class="pink"></span></div>
    <p class="slogan">Your furry friends deserves the best</p>
    <div class="rule bottom"></div>
    <div class="badges">
      <span class="badge green"></span>
      <span class="badge gold"></span>
    </div>
  </section>

</body>
</html>
```